High-End Print/Digital Ad for Unique Luxury Travel Company Required

Objective:
Design a compelling and visually striking advertisement that highlights our company’s unmatched luxury travel experiences. The ad should elevate our brand image, spark curiosity, and drive prospective clients to contact us.
Target Audience:
• Affluent individuals seeking extraordinary, tailor-made travel experiences
• Affluent, luxury, high-net-worth individuals looking for value, expertise, and white-glove service
• Professionals or retirees who appreciate unique, thoughtfully curated travel over mainstream tourism
Key Messages to Communicate:
• One-of-a-kind luxury travel: Once-in-a-lifetime experiences that are curated with creativity and meticulous attention to detail
• Exceptional service: White-glove, personalized planning from start to finish
• 38 years’ travel experience – expert knowledge of destinations, modes of travel, premium accommodations and well-established, meaningful industry connections.
• Highly trusted: Cruise line executives often say, “No one does what you do.”
Tone and Style:
• Elegant, luxurious, sophisticated
• Eye-catching, polished, and modern
• Professional but warm—conveys trust and credibility
• High-impact visuals (full-bleed imagery, custom graphics, or high-end photography)
Deliverables:
• One full-page print ad and digital ad
• Ready-to-print, high-resolution file + working file (PSD, AI, etc.)
Optional: Social media-optimized version or short motion-graphic variation (if designer offers it)
Inspiration & Visual Style Suggestions:
• Think Velvet Voyager, Brimley Hart Wanderer, Seven Lanterns, or Oriel Retreats ad styles
• Large, emotive imagery with elegant typography
• Clean layout that speaks luxury, clarity, and trust
Copy Direction (draft):
For those who’ve explored the world—and crave something beyond the ordinary.
Each journey is a masterfully curated experience, rich in detail, seamless in execution, and unforgettable in every way.
Founded in 1997, Tidewell Journeys is a unique travel company specializing in cruising, all-inclusive luxury properties, and tours world-wide for individuals, groups, and incentives.
We offer an exceptional range of services designed to ensure every journey is flawlessly executed and truly unforgettable.
Let us help you plan your next extraordinary adventure.
Note: You may refine the copy slightly based on layout or format needs.
Other Resources for References:
1. Website - www.tidewelljourneys.example

```html
<!DOCTYPE html>
<html lang="en">
<head>
<meta charset="UTF-8">
<title>Tidewell Journeys – Ad Suite</title>
<link rel="stylesheet" href="https://fonts.googleapis.com/css2?family=Tinos:wght@400;700&family=Montserrat:wght@300;400&display=swap">
<style>
  :root {
    --board: #dcdcdc;
    --ink: #0d0d0d;
    --paper: #ffffff;
    --label: #4a4a4a;
    --rule: #555555;
    --sky-deep: #0b1d3a;
    --sky-mid: #1d4f8f;
    --sky-glow: rgba(90, 150, 225, 0.75);
    --sea: #0a1322;
    --hull: rgba(4, 8, 16, 0.97);
    --deck-light: rgba(255, 214, 140, 1);
    --deck-warm: rgba(232, 150, 58, 0.85);
    --deck-fade: rgba(120, 68, 26, 0.4);
    --reflect: rgba(236, 160, 70, 0.8);
    --reflect-fade: rgba(150, 90, 35, 0.35);
    --serif: "Tinos", "Times New Roman", serif;
    --sans: "Montserrat", Arial, sans-serif;
  }
  * { box-sizing: border-box; margin: 0; padding: 0; }
  html, body { width: 1200px; height: 800px; overflow: hidden; }
  body { background: var(--board); position: relative; font-family: var(--sans); }

  .connectors { position: absolute; inset: 0; }

  .format-label {
    position: absolute; right: 47px;
    font-family: var(--sans); font-weight: 300;
    font-size: 15px; letter-spacing: 0.5px; color: var(--label);
    line-height: 1;
  }
  .format-label--print { top: 51px; }
  .format-label--social { top: 86px; }
  .format-label--banner { top: 120px; }

  .ad { position: absolute; overflow: hidden; background: var(--paper); }

  /* Night-sea scene: starry sky, lit ship decks, dark hull, golden reflection */
  .ad__photo {
    position: absolute; inset: 0;
    background:
      radial-gradient(ellipse var(--ship-w) var(--ship-h) at var(--ship-x) var(--ship-y),
        var(--deck-light) 0%, var(--deck-warm) 38%, var(--deck-fade) 68%, rgba(0,0,0,0) 82%),
      radial-gradient(ellipse calc(var(--ship-w) * 1.08) calc(var(--ship-h) * 1.1) at var(--ship-x) var(--hull-y),
        var(--hull) 0%, var(--hull) 55%, rgba(4,8,16,0) 80%),
      radial-gradient(ellipse calc(var(--ship-w) * 0.95) var(--refl-h) at var(--ship-x) var(--refl-y),
        var(--reflect) 0%, var(--reflect-fade) 50%, rgba(0,0,0,0) 80%),
      radial-gradient(ellipse 45% 28% at 78% 14%, var(--sky-glow), rgba(60,120,200,0) 72%),
      linear-gradient(180deg,
        var(--sky-deep) 0%, var(--sky-mid) 24%, #15375f calc(var(--horizon) - 14%),
        #0b1a2e var(--horizon), #171008 calc(var(--horizon) + 6%), var(--sea) 100%);
  }
  .ad__headline {
    position: absolute; font-family: var(--serif); font-weight: 700;
    color: var(--ink); text-transform: uppercase; letter-spacing: 0.5px;
  }
  .ad__subline {
    position: absolute; font-family: var(--serif); font-weight: 700;
    color: var(--ink); text-transform: uppercase; letter-spacing: 0.6px;
  }
  .brand {
    position: absolute; display: flex; align-items: center; gap: 5px;
    font-family: var(--serif); font-weight: 400; color: var(--paper);
    text-transform: uppercase; letter-spacing: 0.5px; white-space: nowrap;
  }
  .brand__dot { border-radius: 50%; background: var(--paper); display: block; }

  /* Print */
  .ad--print {
    left: 41px; top: 41px; width: 511px; height: 718px;
    --ship-x: 60%; --ship-y: 44%; --ship-w: 50%; --ship-h: 9%;
    --hull-y: 54%; --refl-y: 74%; --refl-h: 10%; --horizon: 63%;
  }
  .ad--print .ad__photo { clip-path: polygon(423px 0, 100% 0, 100% 100%, 0 100%, 0 543px); }
  .ad--print .ad__headline { left: 26px; top: 20px; font-size: 38px; line-height: 39px; }
  .ad--print .ad__subline { left: 26px; top: 176px; font-size: 15.5px; line-height: 20px; }
  .ad__body {
    position: absolute; left: 27px; top: 544px; width: 280px;
    font-family: var(--sans); font-weight: 400; font-size: 10.8px; line-height: 13.4px;
    color: var(--paper); white-space: nowrap;
  }
  .ad__body p + p { margin-top: 14px; }
  .ad--print .brand { left: 27px; top: 669px; font-size: 16px; }
  .ad--print .brand__dot { width: 16px; height: 16px; }

  /* Banner */
  .ad--banner {
    left: 781px; top: 203px; width: 372px; height: 141px;
    --ship-x: 68%; --ship-y: 46%; --ship-w: 28%; --ship-h: 20%;
    --hull-y: 66%; --refl-y: 94%; --refl-h: 12%; --horizon: 84%;
  }
  .ad--banner .ad__photo { clip-path: polygon(259px 0, 100% 0, 100% 100%, 150px 100%); }
  .ad--banner .ad__headline { left: 15px; top: 10px; font-size: 19.5px; line-height: 21px; }
  .ad--banner .ad__subline { left: 15px; top: 96px; font-size: 8.6px; line-height: 10.8px; }
  .ad--banner .brand { right: 10px; top: 9px; font-size: 8px; }
  .ad--banner .brand__dot { width: 8px; height: 8px; }

  /* Social */
  .ad--social {
    left: 781px; top: 387px; width: 372px; height: 372px;
    --ship-x: 58%; --ship-y: 57%; --ship-w: 50%; --ship-h: 11%;
    --hull-y: 70%; --refl-y: 90%; --refl-h: 10%; --horizon: 80%;
  }
  .ad--social .ad__photo { clip-path: polygon(274px 0, 100% 0, 100% 100%, 0 100%, 0 353px); }
  .ad--social .ad__headline { left: 15px; top: 8px; font-size: 25px; line-height: 26.5px; }
  .ad--social .ad__subline { left: 15px; top: 116px; font-size: 11px; line-height: 13.4px; }
  .ad--social .brand { left: 17px; top: 341px; font-size: 12px; }
  .ad--social .brand__dot { width: 12px; height: 12px; }
</style>
</head>
<body>

<svg class="connectors" width="1200" height="800" viewBox="0 0 1200 800" aria-hidden="true">
  <g fill="none" stroke="var(--rule)" stroke-width="1">
    <polyline points="564,58 1066,58"/>
    <polyline points="999,93 699,93 699,398 767,398"/>
    <polyline points="980,127 735,127 735,221 767,221"/>
  </g>
  <g fill="var(--rule)">
    <circle cx="564" cy="58" r="4.5"/>
    <circle cx="767" cy="398" r="4.5"/>
    <circle cx="767" cy="221" r="4.5"/>
  </g>
</svg>

<span class="format-label format-label--print">PRINT AD</span>
<span class="format-label format-label--social">SOCIAL MEDIA AD</span>
<span class="format-label format-label--banner">DIGITAL BANNER AD</span>

<section class="ad ad--print">
  <div class="ad__photo" role="img" aria-label="Photograph of an illuminated luxury cruise ship at night under a starry sky, its golden deck lights reflected on dark water"></div>
  <h1 class="ad__headline">For Those<br>Who’ve<br>Explored<br>The World</h1>
  <p class="ad__subline">And crave something<br>beyond the<br>ordinary.</p>
  <div class="ad__body">
    <p>Each journey is a masterfully curated<br>experience, rich in detail, seamless<br>in execution, and unforgettable in every way.</p>
    <p>We offer an exceptional range of services<br>designed to ensure every journey is flawlessly<br>executed and truly unforgettable.<br>www.tidewelljourneys.example</p>
  </div>
  <div class="brand"><span class="brand__dot"></span>Tidewell Journeys</div>
</section>

<section class="ad ad--banner">
  <div class="ad__photo" role="img" aria-label="Photograph of an illuminated luxury cruise ship at night with golden reflections on the sea"></div>
  <h2 class="ad__headline">For Those<br>Who’ve<br>Explored<br>The World</h2>
  <p class="ad__subline">And crave something<br>beyond the<br>ordinary.</p>
  <div class="brand"><span class="brand__dot"></span>Tidewell Journeys</div>
</section>

<section class="ad ad--social">
  <div class="ad__photo" role="img" aria-label="Photograph of an illuminated luxury cruise ship at night under a starry sky, reflected on dark water"></div>
  <h2 class="ad__headline">For Those<br>Who’ve<br>Explored<br>The World</h2>
  <p class="ad__subline">And crave something<br>beyond the<br>ordinary.</p>
  <div class="brand"><span class="brand__dot"></span>Tidewell Journeys</div>
</section>

</body>
</html>
```